Redesign of Medical App for Patients

• The Designer’s task is to provide a new fully-responsive design for our apps, and then code it using only basic html and CSS.
• Your design will be incorporated into our existing REACT native app.

Target Market(s)

Medical Patients

Industry/Entity Type

Medical

Coding

Coded - Design and coding required

Number of Pages Required

5+ page

Requirements
Must have
• Short list candidates will receive detailed briefing
Nice to have
• detailed briefing contains some of our ideas.

```html
<!DOCTYPE html>
<html lang="en">
<head>
<meta charset="utf-8">
<title>Patient App Screens</title>
<link href="https://fonts.googleapis.com/css2?family=Roboto:wght@400;500;700&display=swap" rel="stylesheet">
<style>
:root{
  --blue:#1b93c9;
  --blue-dark:#117aab;
  --ink:#111;
  --muted:#6d6d6d;
  --pill:#f3f4f6;
  --bg:#e4e8ec;
  --white:#fff;
}
*{box-sizing:border-box;margin:0;padding:0}
html,body{width:1200px;height:850px;overflow:hidden}
body{background:var(--bg);font-family:'Roboto',sans-serif;color:var(--ink);
  display:flex;justify-content:space-evenly;align-items:center}
.screen{width:330px;height:740px;background:var(--white);border-radius:26px;overflow:hidden;
  display:flex;flex-direction:column;box-shadow:0 8px 30px rgba(0,0,0,.12)}
.status{display:flex;justify-content:space-between;align-items:center;padding:18px 24px 0;font-size:13px;font-weight:500}
.brand{display:flex;align-items:center;justify-content:center;gap:10px;margin-top:12px}
.brand-dot{width:32px;height:32px;border-radius:50%;background:var(--blue)}
.brand-name{font-size:23px;font-weight:500;color:var(--blue-dark);letter-spacing:.3px}
.content{flex:1;padding:0 20px;overflow:hidden}
.page-title{font-size:24px;font-weight:500;text-align:center;margin-top:8px}
.photo{border-radius:12px;margin-top:16px}
.photo-organ{height:212px;background:radial-gradient(circle at 55% 50%,#b5605c,#d2783a 45%,#8a3b1e)}
.photo-ward{height:132px;border-radius:4px;margin-top:12px;background:linear-gradient(120deg,#8fb6c9,#d9dde0 50%,#7fb4d4)}
.about h2{font-size:24px;font-weight:500;margin-top:28px}
.q{font-size:13.5px;font-weight:500;margin-top:12px}
.q.active{color:var(--blue)}
.about p{font-size:13px;line-height:23px;color:var(--muted);text-align:justify;margin-top:8px}
.tabs{display:flex;gap:8px;margin-top:16px}
.tab{flex:1;height:34px;border-radius:8px;display:flex;align-items:center;justify-content:center;font-size:14px;
  box-shadow:0 2px 10px rgba(0,0,0,.1)}
.tab.on{background:var(--blue);color:#fff;font-weight:500}
.check-link{display:flex;justify-content:center;align-items:center;gap:8px;color:var(--blue);font-size:14px;font-weight:500;margin:20px 0 26px}
.acc{background:var(--pill);border-radius:14px;padding:11px 16px;margin-bottom:13px;font-size:13px;font-weight:500}
.acc-head{display:flex;justify-content:space-between;align-items:center}
.acc.open .acc-head{color:var(--blue);font-weight:400}
.acc-body{font-size:13px;line-height:21px;color:var(--muted);margin-top:10px;text-align:justify;font-weight:400}
.acc-body b{color:var(--ink);font-weight:500}
.recovery .acc{padding:10px 16px;margin-bottom:10px}
.acc-body.small{font-size:11.5px;line-height:19px;color:#333;margin-top:8px}
.chev{width:13px;height:13px;flex:none}
.nav{height:60px;flex:none;background:var(--blue);display:flex;justify-content:space-around;align-items:center;padding:0 24px}
.nav-btn{width:40px;height:40px;border-radius:50%;display:flex;align-items:center;justify-content:center}
.nav-btn.on{background:var(--blue-dark)}
.nav svg{width:18px;height:18px}
</style>
</head>
<body>

<svg width="0" height="0" style="position:absolute">
  <defs>
    <symbol id="down" viewBox="0 0 14 14"><circle cx="7" cy="7" r="7" fill="#1b93c9"/><path d="M4 6l3 3 3-3" stroke="#fff" stroke-width="1.8" fill="none"/></symbol>
    <symbol id="up" viewBox="0 0 14 14"><circle cx="7" cy="7" r="7" fill="#1b93c9"/><path d="M4 8.5l3-3 3 3" stroke="#fff" stroke-width="1.8" fill="none"/></symbol>
    <symbol id="home" viewBox="0 0 20 20"><path d="M10 2L1 10h3v8h5v-5h2v5h5v-8h3z" fill="#fff"/></symbol>
    <symbol id="user" viewBox="0 0 20 20"><circle cx="10" cy="6" r="4" fill="#fff"/><path d="M3 19c0-5 3-7 7-7s7 2 7 7z" fill="#fff"/></symbol>
    <symbol id="back" viewBox="0 0 20 20"><circle cx="10" cy="10" r="9" fill="#fff"/><path d="M11.5 5.5L7 10l4.5 4.5M7 10h7" stroke="#1b93c9" stroke-width="2.2" fill="none"/></symbol>
    <symbol id="fwd" viewBox="0 0 20 20"><circle cx="10" cy="10" r="9" fill="#fff"/><path d="M8.5 5.5L13 10l-4.5 4.5M13 10H6" stroke="#1b93c9" stroke-width="2.2" fill="none"/></symbol>
    <symbol id="gear" viewBox="0 0 20 20">
      <g fill="#fff">
        <rect x="8" y="1" width="4" height="18" rx="1"/>
        <rect x="8" y="1" width="4" height="18" rx="1" transform="rotate(45 10 10)"/>
        <rect x="8" y="1" width="4" height="18" rx="1" transform="rotate(90 10 10)"/>
        <rect x="8" y="1" width="4" height="18" rx="1" transform="rotate(135 10 10)"/>
        <circle cx="10" cy="10" r="6.5"/>
      </g>
      <circle cx="10" cy="10" r="2.5" fill="#1b93c9"/>
    </symbol>
    <symbol id="sig" viewBox="0 0 50 10"><path d="M2 9h2V7H2zM5 9h2V5H5zM8 9h2V2H8z" fill="#111"/><path d="M20 4a7 7 0 0 1 10 0M22 6a4 4 0 0 1 6 0" stroke="#111" stroke-width="1.4" fill="none"/><circle cx="25" cy="8.5" r="1.2" fill="#111"/><rect x="37" y="2" width="11" height="6.5" rx="1.2" fill="none" stroke="#111"/><rect x="38.5" y="3.5" width="7" height="3.5" fill="#111"/></symbol>
  </defs>
</svg>

<!-- About -->
<section class="screen">
  <div class="status"><span>12:48</span><svg viewBox="0 0 50 10" width="50" height="10"><use href="#sig"/></svg></div>
  <div class="brand"><span class="brand-dot"></span><span class="brand-name">KESTRAVIA</span></div>
  <div class="content about">
    <div class="photo photo-organ" role="img" aria-label="Illustration of a stomach with a gallstone"></div>
    <h2>About Procedure</h2>
    <div class="q">Is it too late to prevent gallbladder disease?</div>
    <div class="q active">What will happen if I don't have this procedure?</div>
    <p>If you chose not to undergo surgery and do not adopt other solutions - it is likely that your pain will persist. There is also a chance that your pain will worsen and could even lead to infection and perforation of the gallbladder requiring more risky emergency surgery.</p>
    <div class="q">Are there alternative solutions?</div>
    <div class="q">What are the risks of this procedure?</div>
  </div>
  <nav class="nav">
    <span class="nav-btn on"><svg><use href="#home"/></svg></span>
    <span class="nav-btn"><svg><use href="#user"/></svg></span>
    <span class="nav-btn"><svg><use href="#back"/></svg></span>
    <span class="nav-btn"><svg><use href="#fwd"/></svg></span>
    <span class="nav-btn"><svg><use href="#gear"/></svg></span>
  </nav>
</section>

<!-- Pre-procedure -->
<section class="screen">
  <div class="status"><span>12:48</span><svg viewBox="0 0 50 10" width="50" height="10"><use href="#sig"/></svg></div>
  <div class="brand"><span class="brand-dot"></span><span class="brand-name">KESTRAVIA</span></div>
  <div class="content">
    <h1 class="page-title">Pre- Procedure</h1>
    <div class="tabs"><span class="tab on">Weeks Before</span><span class="tab">Day Before</span></div>
    <div class="check-link"><svg width="13" height="13" viewBox="0 0 14 14"><rect x="1" y="2" width="10" height="10" rx="2" fill="none" stroke="#1b93c9" stroke-width="1.6"/><path d="M4 7l2.5 2.5L13 2" stroke="#1b93c9" stroke-width="1.8" fill="none"/></svg>Check When Task Is Completed</div>
    <div class="acc"><div class="acc-head">Pre-operative appointment<svg class="chev"><use href="#down"/></svg></div></div>
    <div class="acc"><div class="acc-head">8weeks before (or after your pre<svg class="chev"><use href="#down"/></svg></div></div>
    <div class="acc open"><div class="acc-head">6 weeks before<svg class="chev"><use href="#up"/></svg></div>
      <div class="acc-body"><b>Discontinue smoking and nicotine use</b> If smoking cessation is challenging, nicotine replacement therapy is still better than smoking (even though nicotine should also be avoided).</div></div>
    <div class="acc"><div class="acc-head">2 weeks before<svg class="chev"><use href="#down"/></svg></div></div>
    <div class="acc"><div class="acc-head">1 weeks before<svg class="chev"><use href="#down"/></svg></div></div>
  </div>
  <nav class="nav">
    <span class="nav-btn on"><svg><use href="#home"/></svg></span>
    <span class="nav-btn"><svg><use href="#user"/></svg></span>
    <span class="nav-btn"><svg><use href="#back"/></svg></span>
    <span class="nav-btn"><svg><use href="#fwd"/></svg></span>
    <span class="nav-btn"><svg><use href="#gear"/></svg></span>
  </nav>
</section>

<!-- Recovery -->
<section class="screen">
  <div class="status"><span>12:48</span><svg viewBox="0 0 50 10" width="50" height="10"><use href="#sig"/></svg></div>
  <div class="brand"><span class="brand-dot"></span><span class="brand-name">KESTRAVIA</span></div>
  <div class="content recovery">
    <h1 class="page-title" style="margin-top:4px">Recovery</h1>
    <div class="photo photo-ward" role="img" aria-label="Photo of a nurse checking a monitor beside a patient resting in a hospital bed"></div>
    <div class="acc open" style="margin-top:14px"><div class="acc-head">When do I leave the Hospital?<svg class="chev"><use href="#up"/></svg></div>
      <div class="acc-body small">The recovery process is typically uncomplicated and straightforward. Most patients go home on the same day of their surgery. However, if your surgery was converted to an open procedure, or there were complications, or your surgeon simply wants to look after you for more than just a few hours, you may need to stay overnight.</div></div>
    <div class="acc"><div class="acc-head">Waking up<svg class="chev"><use href="#down"/></svg></div></div>
    <div class="acc"><div class="acc-head">Pain management<svg class="chev"><use href="#down"/></svg></div></div>
    <div class="acc"><div class="acc-head">Same-day Discharge<svg class="chev"><use href="#down"/></svg></div></div>
    <div class="acc"><div class="acc-head">Ready to leave<svg class="chev"><use href="#down"/></svg></div></div>
  </div>
  <nav class="nav">
    <span class="nav-btn"><svg><use href="#home"/></svg></span>
    <span class="nav-btn"><svg><use href="#user"/></svg></span>
    <span class="nav-btn on"><svg><use href="#back"/></svg></span>
    <span class="nav-btn"><svg><use href="#fwd"/></svg></span>
    <span class="nav-btn"><svg><use href="#gear"/></svg></span>
  </nav>
</section>

</body>
</html>
```